Conservative, Modern and Sharp Builder Business card

Hi there,
We would like to update our existing business card.
I have attached photos of existing business card, logo and van sign.

I would like the business card to also list what we do :
Renovation • New Build • Alteration
Extension • Bathroom • Maintenance.(Seperated by dots)

Contact number : 021 0483 0752
(With that exact spacing)

Ideally when people looking from about 2-3 metres, they know that it is a builder’s business card

Open to suggestions on fonts, layout, style of business card

PLEASE ONLY SUBMIT YOUR BEST OR MAX 3 DESIGNS FOR EACH DESIGNER

Thanks

Industry/Entity Type

Construction. Renovation

Contact Information for Business Card

Details should be the same as the existing card. And addition of what we do.

Requirements
Should not have
• The new business card must not have the same layout as our existing one. Thanks

```html
<!DOCTYPE html>
<html lang="en">
<head>
<meta charset="utf-8">
<title>KeelBuild Business Card</title>
<link href="https://fonts.googleapis.com/css2?family=Source+Sans+3:wght@600;700&display=swap" rel="stylesheet">
<style>
  :root {
    --bg-light: #a1a2a6;
    --bg-dark: #87888c;
    --ink: #000000;
    --paper: #ffffff;
    --haze: #d6d6d6;
    --shadow: rgba(0, 0, 0, 0.38);
  }
  html, body {
    margin: 0;
    padding: 0;
    overflow: hidden;
  }
  body {
    width: 988px;
    height: 1200px;
    position: relative;
    background: var(--bg-light);
    font-family: "Source Sans 3", "Source Sans Pro", Arial, sans-serif;
  }
  .backdrop-shade {
    position: absolute;
    inset: 0;
    background: var(--bg-dark);
    clip-path: polygon(910px 0, 988px 0, 988px 1200px, 82px 1200px);
  }
  .card {
    position: absolute;
    width: 840px;
    height: 476px;
    border-radius: 32px;
    overflow: hidden;
    box-shadow: 6px 8px 10px var(--shadow);
  }
  .card-front {
    left: 66px;
    top: 94px;
    background: var(--ink);
    color: var(--paper);
  }
  .card-back {
    left: 74px;
    top: 627px;
    background: var(--paper);
    color: var(--ink);
  }
  .brand-square {
    position: absolute;
    background: currentColor;
  }
  .card-front .brand-square {
    left: 398px;
    top: 110px;
    width: 60px;
    height: 60px;
  }
  .brand-name {
    position: absolute;
    margin: 0;
    font-weight: 700;
    line-height: 1;
    text-align: center;
    letter-spacing: -0.5px;
  }
  .card-front .brand-name {
    left: 0;
    width: 840px;
    top: 240px;
    font-size: 88px;
  }
  .website {
    position: absolute;
    left: 0;
    width: 840px;
    top: 404px;
    text-align: center;
    font-size: 27px;
    font-weight: 600;
    letter-spacing: 11px;
    line-height: 1.2;
  }
  .card-back .brand-square {
    left: 215px;
    top: 128px;
    width: 38px;
    height: 38px;
  }
  .card-back .brand-name {
    left: 40px;
    width: 386px;
    top: 222px;
    font-size: 68px;
  }
  .contact {
    position: absolute;
    left: 483px;
    top: 0;
  }
  .person-name {
    position: absolute;
    left: 0;
    top: 44px;
    margin: 0;
    font-size: 38px;
    font-weight: 700;
    white-space: nowrap;
    line-height: 1;
  }
  .person-role,
  .address-line,
  .contact-row {
    position: absolute;
    left: 0;
    font-size: 19px;
    font-weight: 600;
    white-space: nowrap;
    line-height: 24px;
  }
  .person-role { top: 102px; letter-spacing: 0.3px; }
  .address-line.first { top: 143px; }
  .address-line.second { top: 180px; }
  .contact-row {
    display: flex;
    align-items: center;
    gap: 16px;
  }
  .contact-row svg {
    width: 24px;
    height: 24px;
    flex: none;
  }
  .row-phone { top: 225px; }
  .row-mail { top: 264px; }
  .row-social { top: 305px; }
  .roof-artwork {
    position: absolute;
    left: 88px;
    top: 352px;
    width: 668px;
    height: 58px;
    background: linear-gradient(to bottom, var(--haze), var(--ink));
  }
  .service-band {
    position: absolute;
    left: 0;
    top: 410px;
    width: 840px;
    height: 66px;
    background: var(--ink);
  }
  .service-band svg {
    display: block;
    width: 840px;
    height: 66px;
  }
  .services {
    font-family: "Source Sans 3", "Source Sans Pro", Arial, sans-serif;
    font-weight: 700;
    font-size: 19px;
    fill: var(--paper);
  }
</style>
</head>
<body>
  <div class="backdrop-shade"></div>

  <section class="card card-front">
    <div class="brand-square"></div>
    <h1 class="brand-name">KeelBuild</h1>
    <div class="website">www.keelbuild.nz</div>
  </section>

  <section class="card card-back">
    <div class="brand-square"></div>
    <h1 class="brand-name">KeelBuild</h1>

    <div class="contact">
      <h2 class="person-name">Tomas Varga</h2>
      <div class="person-role">RESIDENTIAL BUILDER</div>
      <div class="address-line first">42 Kauri Street, Eastbourne,</div>
      <div class="address-line second">Lower Hutt 5013, NZ</div>

      <div class="contact-row row-phone">
        <svg viewBox="0 0 24 24" aria-hidden="true">
          <path d="M6.6 2.5c.6-.4 1.4-.3 1.8.3l2.1 3.1c.4.6.3 1.3-.2 1.8L8.9 9c.9 2.4 3.2 4.7 5.6 5.6l1.3-1.4c.5-.5 1.2-.6 1.8-.2l3.1 2.1c.6.4.7 1.2.3 1.8l-1.3 2c-.8 1.2-2.3 1.7-3.700 1.2C9.6 18 5.9 14.3 3.9 8.9c-.5-1.4 0-2.9 1.2-3.7z" fill="var(--ink)"/>
          <path d="M14 3.5a6.5 6.5 0 0 1 6.5 6.5M14 6.5a3.5 3.5 0 0 1 3.5 3.5" stroke="var(--ink)" stroke-width="1.6" fill="none" stroke-linecap="round"/>
        </svg>
        <span>021 0483 0752</span>
      </div>

      <div class="contact-row row-mail">
        <svg viewBox="0 0 24 24" aria-hidden="true">
          <rect x="2" y="5" width="20" height="14" fill="var(--ink)"/>
          <path d="M2.5 5.5 12 13l9.5-7.5M2.5 18.5 9.5 11.5M21.5 18.5l-7-7" stroke="var(--paper)" stroke-width="1.5" fill="none"/>
        </svg>
        <span>hello@keelbuild.co.nz</span>
      </div>

      <div class="contact-row row-social">
        <svg viewBox="0 0 24 24" aria-hidden="true">
          <circle cx="12" cy="12" r="9.5" stroke="var(--ink)" stroke-width="2.2" fill="none"/>
        </svg>
        <span>keelbuild.nz</span>
      </div>
    </div>

    <div class="roof-artwork" role="img" aria-label="Decorative roofline artwork in black"></div>

    <div class="service-band">
      <svg viewBox="0 0 840 66" aria-label="Services">
        <text class="services" x="420" y="40" text-anchor="middle" textLength="770" lengthAdjust="spacingAndGlyphs">RENOVATION • NEW BUILD • ALTERATION • EXTENSION • BATHROOM • MAINTENANCE</text>
      </svg>
    </div>
  </section>
</body>
</html>
```